Brightford Lingua Partners, LLC

We need a business card that includes information about our business and conveys a reliable business that provides document translation services and interpreters for a variety of corporate and individual clients. We want to come across as professional, reliable, yet approachable. It should include the following on one side:

ESL / ENL Language Classes, Private Lessons, and Online Tutors
PALQE Training and Testing
Translating & Interpreting Services
Contact us about Over-the-Phone Interpreting in over 200 languages
24/7/365
www.brightfordlingua.example

The other side should include (555) 481-3062

Marla Quennick, President
412 Garvin Ave., Ste. 209
Indianapolis, IN 46999
Updates

Please add USA as part of the address. Also, please add mrqquennick@brightfordlinguapartners.example as the e-mail address. Thank you.

Target Market(s)

Business professionals, their families, the international community

Industry/Entity Type

Business

Contact Information for Business Card

24/7/365
www.brightfordlingua.example

(555) 481-3062

Marla Quennick, President
412 Garvin Ave., Ste. 209
Indianapolis, IN 46999
USA

Font styles to use
Sans Serif

Colors

Designer to choose colors to be used in the design.

Requirements
Must have
• See project description
• e-mail address and web address
• Phone number
Nice to have
• a globe
• physical address
Should not have
• Should not have the same color scheme as other agencies in our market in Indiana unless it is blue and black. No purple or yellow.

```html
<!DOCTYPE html>
<html lang="en">
<head>
<meta charset="utf-8">
<title>Brightford Lingua Partners – Business Card</title>
<link href="https://fonts.googleapis.com/css2?family=Arimo:wght@400;700&family=Lato:wght@400;700&display=swap" rel="stylesheet">
<style>
  :root {
    --brand-blue: #2a96d4;
    --ink: #111111;
    --paper: #ffffff;
    --stage: #e9ebee;
    --map-tone: #f1f2f4;
  }
  * { box-sizing: border-box; margin: 0; padding: 0; }
  html, body { width: 1189px; height: 1200px; overflow: hidden; background: var(--stage); }
  body { position: relative; font-family: "Arimo", Arial, sans-serif; color: var(--ink); }

  .card {
    position: absolute; left: 167px; width: 854px; height: 488px;
    background: var(--paper); border-radius: 40px; overflow: hidden;
    box-shadow: 0 6px 18px rgba(0,0,0,.12);
  }
  .card--front { top: 67px; }
  .card--back { top: 625px; }

  .world-backdrop {
    position: absolute; left: 80px; top: 80px; width: 700px; height: 340px;
    background: radial-gradient(ellipse at center, var(--map-tone) 0%, rgba(241,242,244,0) 70%);
  }

  .brand { position: absolute; display: flex; align-items: center; }
  .brand__dot { width: 150px; height: 150px; border-radius: 50%; background: var(--brand-blue); flex: none; }
  .brand__name {
    font-family: "Lato", sans-serif; font-weight: 700; color: var(--ink);
    font-size: 34px; line-height: 44px; margin-left: 12px;
  }
  .card--front .brand { left: 252px; top: 86px; }
  .card--back .brand { left: 475px; top: 46px; }
  .card--back .brand__dot { width: 144px; height: 144px; }
  .card--back .brand__name { font-size: 33px; line-height: 42px; }

  .services {
    position: absolute; left: 0; right: 0; top: 266px; text-align: center;
    font-size: 21px; line-height: 27px; color: var(--ink);
  }
  .website-line {
    position: absolute; left: 0; right: 0; top: 377px; text-align: center;
    font-size: 19px; letter-spacing: 3px;
  }
  .website-line .accent { color: var(--brand-blue); }
  .phone-band {
    position: absolute; left: 0; right: 0; top: 419px; height: 45px;
    background: var(--brand-blue); color: var(--paper);
    font-size: 20px; line-height: 45px; text-align: center;
  }

  .edge-tab {
    position: absolute; left: -28px; top: 41px; width: 56px; height: 56px;
    border-radius: 50%; background: var(--brand-blue);
  }
  .holder { position: absolute; left: 39px; top: 40px; }
  .holder__name { font-family: "Lato", sans-serif; font-weight: 700; font-size: 29px; line-height: 34px; }
  .holder__title { color: var(--brand-blue); font-size: 21px; line-height: 24px; }

  .rule { position: absolute; left: 41px; width: 773px; top: 336px; border-top: 2px solid var(--brand-blue); }

  .contacts { position: absolute; left: 39px; top: 361px; list-style: none; }
  .contacts li { display: flex; align-items: center; height: 31px; font-size: 19px; }
  .contacts svg { width: 26px; height: 26px; margin-right: 12px; flex: none; }

  .address {
    position: absolute; right: 40px; top: 395px; text-align: right;
    font-size: 19px; line-height: 31px; font-style: normal;
  }
</style>
</head>
<body>

<section class="card card--front" aria-label="Card front">
  <div class="world-backdrop" role="img" aria-label="Faint world map in the background"></div>
  <div class="brand">
    <div class="brand__dot"></div>
    <div class="brand__name">Brightford<br>Lingua<br>Partners, LLC</div>
  </div>
  <div class="services">
    <p>ESL / ENL Language Classes | Private Lessons and Online Tutors</p>
    <p>PALQE Training and Testing</p>
    <p>Translating &amp; Interpreting Services</p>
  </div>
  <p class="website-line">www.<span class="accent">brightfordlingua</span>.example</p>
  <p class="phone-band">Contact us about Over-the-Phone Interpreting in over 200 languages 24/7/365</p>
</section>

<section class="card card--back" aria-label="Card back">
  <div class="edge-tab"></div>
  <div class="holder">
    <p class="holder__name">Marla Quennick</p>
    <p class="holder__title">President</p>
  </div>
  <div class="brand">
    <div class="brand__dot"></div>
    <div class="brand__name">Brightford<br>Lingua<br>Partners, LLC</div>
  </div>

  <div class="rule"></div>

  <ul class="contacts">
    <li>
      <svg viewBox="0 0 26 26" aria-hidden="true"><circle cx="13" cy="13" r="13" fill="var(--brand-blue)"/><path d="M7 11c0-2 3-3 6-3s6 1 6 3l-2 1-1-1.5h-6L9 12zM9 13h8l1 5H8z" fill="#fff"/></svg>
      (555) 481-3062
    </li>
    <li>
      <svg viewBox="0 0 26 26" aria-hidden="true"><circle cx="13" cy="13" r="13" fill="var(--brand-blue)"/><rect x="7" y="9" width="12" height="9" fill="none" stroke="#fff" stroke-width="1.5"/><path d="M7 9l6 5 6-5M7 18l4.5-4.5M19 18l-4.5-4.5" fill="none" stroke="#fff" stroke-width="1.3"/></svg>
      mrqquennick@brightfordlinguapartners.example
    </li>
    <li>
      <svg viewBox="0 0 26 26" aria-hidden="true"><circle cx="13" cy="13" r="13" fill="var(--brand-blue)"/><g fill="none" stroke="#fff" stroke-width="1.3"><circle cx="13" cy="13" r="7"/><ellipse cx="13" cy="13" rx="3" ry="7"/><path d="M6 13h14M7.5 9.5h11M7.5 16.5h11"/></g></svg>
      www.brightfordlingua.example
    </li>
  </ul>

  <address class="address">412 Garvin Ave., Ste. 209<br>Indianapolis, IN 46999, USA</address>
</section>

</body>
</html>
```